Bright K's Auto Detailing new business cards

I am a business owner who professionally details cars. I clean and detail the interiors, exteriors of vehicles. I need a logo designed for my new business Bright K's Auto Detailing and a great designed card that will wow anyone that I hand it out to. Attached is a photo that I would like on side of the card. I want the picture to be on the right side of the card, while my busines name will be on the other side. I want the picture to have a slant where it divided the card into left and right, not just straight down. The picture will be printed glossy and I want the left half to have a carbon fiber background. Feel free to design a cool font for the business name, The business name needs to be a red gloss to pop out against the matte background. The back of the card should have my name Colin Marchetti. Under my name should be Owner/ Operator. then all my contact info and fb and instagram stuff. must include services offered- Paint Correction, Exterior detailing
Interior Detailing, Engine Bay Detailing, Headlight restoration, Ceramic Coatings

Target Market(s)

My target market is anyone who drives a vehicle.

Industry/Entity Type

Automotive

Contact Information for Business Card

Business name- Bright K's Auto Detailing
Colin Marchetti Owner/ Operator
Location- Harlow Vale, ST
Business # (555) 214-6079
email- colin@thebrightpolisher.example
fb and instragram logos- @thebrightpolisher

Font styles to use
Serif
Script
Other font styles liked:
• Blacksword

Colors
ec1f27
000000

Requirements
Must have
• The card must be in landscape position. All the details that are in the brief description which are my business name, my name, services offered and any other info thats in the project description. I uploaded pics of veltranos that I would like to see different designs incorporated into the backside of the card. File 5,6,and 7 are ideas that I would like to see done with my business name. The diamond around my name with the polisher coming around the bottom, and a Veltrano outline on the left side of the diamond kinda like file 5
• Also, business name and name should be in some style of script, while the rest of the fonts in serif. Must have the picture of me on the front right side of the card!!!
Nice to have
• Your own personal ideas that you think I am missing.
Should not have
• No grafitti, no generic logos around the business name like every other auto detail card on google.

```html
<!DOCTYPE html>
<html lang="en">
<head>
<meta charset="utf-8">
<title>Bright K's Auto Detailing – Business Cards</title>
<link rel="stylesheet" href="https://fonts.googleapis.com/css2?family=EB+Garamond:wght@400;500&display=swap">
<style>
  :root {
    --red: #ec1f27;
    --black: #000000;
    --stage: #1b1b1c;
    --card: #141415;
    --card-edge: #262628;
    --text-light: #d6d6d6;
    --text-muted: #a9a9a9;
    --photo-deep: #1c2744;
    --photo-mid: #3b4f78;
    --photo-light: #a9b6cf;
  }
  * { box-sizing: border-box; margin: 0; padding: 0; }
  html, body {
    width: 1200px; height: 1120px; overflow: hidden;
    background: var(--stage);
    font-family: "EB Garamond", Georgia, serif;
  }
  .sheet {
    width: 1200px; height: 1120px;
    display: flex; flex-direction: column; align-items: center; justify-content: center;
    gap: 56px;
  }
  .card {
    position: relative;
    width: 840px; height: 480px;
    background: var(--card);
    border: 1px solid var(--card-edge);
    overflow: hidden;
  }

  /* Back side */
  .card-back__scene {
    position: absolute; inset: 0;
    background: radial-gradient(ellipse at 50% 55%, #2c2c2e 0%, #19191a 45%, #0e0e0f 100%);
  }
  .card-back__contact {
    position: absolute; left: 70px; top: 150px;
  }
  .holder-name {
    color: var(--red); font-size: 40px; font-weight: 500; line-height: 1;
  }
  .holder-role {
    color: var(--text-muted); font-size: 23px; margin-top: 6px;
  }
  .contact-list { list-style: none; margin-top: 40px; }
  .contact-list li {
    display: flex; align-items: center; gap: 14px;
    color: var(--text-light); font-size: 22px; line-height: 1.45;
  }
  .contact-icon { width: 22px; height: 22px; flex: none; }
  .social-dot {
    width: 22px; height: 22px; border-radius: 50%; background: var(--red); flex: none;
  }
  .services {
    position: absolute; left: 500px; top: 108px;
    list-style: none;
  }
  .services li {
    color: var(--text-light); font-size: 22px; line-height: 1.6;
    display: flex; align-items: center; gap: 16px;
  }
  .services li::before {
    content: ""; width: 6px; height: 6px; border-radius: 50%; background: var(--red);
  }

  /* Front side */
  .card-front__texture {
    position: absolute; inset: 0;
    background: linear-gradient(135deg, #202022 0%, #111112 60%, #0b0b0c 100%);
  }
  .brand {
    position: absolute; left: 60px; top: 0; bottom: 0; width: 450px;
    display: flex; align-items: center; gap: 14px;
  }
  .brand-mark {
    width: 26px; height: 26px; border-radius: 50%; background: var(--red); flex: none;
  }
  .brand-name {
    color: var(--red); font-size: 36px; font-weight: 500; line-height: 1.1;
    white-space: nowrap;
  }
  .photo-divider {
    position: absolute; top: 0; bottom: 0; left: 520px; width: 8px;
    background: var(--red);
  }
  .photo {
    position: absolute; top: 0; bottom: 0; left: 528px; right: 0;
    background: linear-gradient(160deg, var(--photo-deep) 0%, var(--photo-mid) 55%, var(--photo-light) 100%);
  }
</style>
</head>
<body>
<main class="sheet">

  <section class="card card-back" aria-label="Card back">
    <div class="card-back__scene" role="img" aria-label="Faint photo of a dark sports car in a garage"></div>

    <div class="card-back__contact">
      <h1 class="holder-name">Colin Marchetti</h1>
      <p class="holder-role">Owner/ Operator</p>
      <ul class="contact-list">
        <li>
          <svg class="contact-icon" viewBox="0 0 24 24" aria-hidden="true"><path d="M12 2a7 7 0 0 0-7 7c0 5 7 13 7 13s7-8 7-13a7 7 0 0 0-7-7zm0 9.5A2.5 2.5 0 1 1 12 6.5a2.5 2.5 0 0 1 0 5z" fill="#ec1f27"/></svg>
          Harlow Vale, ST
        </li>
        <li>
          <svg class="contact-icon" viewBox="0 0 24 24" aria-hidden="true"><path d="M6.6 10.8a15 15 0 0 0 6.6 6.6l2.2-2.2a1 1 0 0 1 1-.25 11.4 11.4 0 0 0 3.6.57 1 1 0 0 1 1 1V20a1 1 0 0 1-1 1A17 17 0 0 1 3 4a1 1 0 0 1 1-1h3.5a1 1 0 0 1 1 1c0 1.25.2 2.450.57 3.570a1 1 0 0 1-.25 1z" fill="#ec1f27"/></svg>
          (555) 214-6079
        </li>
        <li>
          <svg class="contact-icon" viewBox="0 0 24 24" aria-hidden="true"><rect x="2" y="5" width="20" height="14" rx="2" fill="#ec1f27"/><path d="M3 6l9 7 9-7" stroke="#141415" stroke-width="1.6" fill="none"/></svg>
          colin@thebrightpolisher.example
        </li>
        <li>
          <span class="social-dot" aria-hidden="true"></span>
          @thebrightpolisher
        </li>
      </ul>
    </div>

    <ul class="services">
      <li>Paint Correction</li>
      <li>Exterior detailing</li>
      <li>Interior Detailing</li>
      <li>Engine Bay Detailing</li>
      <li>Headlight restoration</li>
      <li>Ceramic Coatings</li>
    </ul>
  </section>

  <section class="card card-front" aria-label="Card front">
    <div class="card-front__texture" role="img" aria-label="Dark carbon fiber texture"></div>
    <div class="brand">
      <span class="brand-mark" aria-hidden="true"></span>
      <p class="brand-name">Bright K's Auto Detailing</p>
    </div>
    <div class="photo-divider" aria-hidden="true"></div>
    <div class="photo" role="img" aria-label="Photo of the owner polishing a car with a machine polisher"></div>
  </section>

</main>
</body>
</html>
```